Building Servicess

We need a new business card design for a company. We specialise in: Electrical/Site temporary electrics, Data/Network Installation, Passive Fire Protection

Industry/Entity Type

Construction

Contact Information for Business Card

Services provided as detailed on project description

Font styles to use
Serif

Colors
0054AA
0677BA
7BADD7
CADEEF
E8F1F8
00AB8E
00BBA5
67D7C9
C6EFE9
E9F9F6
EB3D1F
EC4F4E
F09395
F8D3D4
FCEDEE

Requirements
Must have
• Company logo-contact details-phone numbers

```html
<!DOCTYPE html>
<html lang="en">
<head>
<meta charset="utf-8">
<title>Brightline Site Services – Business Card</title>
<link href="https://fonts.googleapis.com/css2?family=Roboto:wght@400;500;700&display=swap" rel="stylesheet">
<style>
  :root {
    --backdrop: #2a2a2a;
    --blue-top: #0a70b4;
    --blue-bottom: #0664a8;
    --band-blue: #0a6cb0;
    --band-blue-dark: #085f9f;
    --logo-blue: #0a63ad;
    --paper: #f1f1f1;
    --paper-shade: #e2e2e2;
    --ink: #1f1f1f;
    --white: #ffffff;
    --soft-white: #e6eff7;
    --rule: #b9d0e6;
  }
  html, body {
    margin: 0;
    padding: 0;
    width: 1200px;
    height: 1138px;
    overflow: hidden;
    background: var(--backdrop);
    font-family: "Roboto", Arial, sans-serif;
  }
  .canvas { position: relative; width: 1200px; height: 1138px; }
  .card {
    position: absolute;
    border-radius: 16px;
    overflow: hidden;
  }
  /* Front */
  .card-front {
    left: 274px; top: 186px; width: 623px; height: 376px;
    background: linear-gradient(180deg, var(--blue-top), var(--blue-bottom));
  }
  .front-name {
    position: absolute; left: 0; right: 0; top: 138px;
    text-align: center; color: var(--white);
    font-size: 34px; font-weight: 700; line-height: 46px;
    letter-spacing: 0.5px;
  }
  .specialise {
    position: absolute; left: 0; right: 0; top: 308px;
    text-align: center; color: var(--soft-white);
    font-size: 16px; line-height: 20px;
  }
  .specialise strong { font-weight: 700; }
  .specialise .sep { margin: 0 6px; }
  /* Back */
  .card-back {
    left: 276px; top: 608px; width: 618px; height: 374px;
    background: linear-gradient(180deg, var(--paper), var(--paper-shade));
  }
  .brand {
    position: absolute; left: 0; right: 0; top: 46px;
    display: flex; justify-content: center; align-items: center; gap: 14px;
  }
  .brand-square { width: 34px; height: 34px; background: var(--logo-blue); }
  .brand-name {
    color: var(--logo-blue); font-size: 30px; font-weight: 700; line-height: 40px;
  }
  .info-band {
    position: absolute; left: 0; top: 138px; width: 100%; height: 180px;
    background: linear-gradient(180deg, var(--band-blue), var(--band-blue-dark));
    color: var(--white);
  }
  .person-name {
    position: absolute; left: 47px; top: 24px;
    font-size: 24px; font-weight: 700; line-height: 28px;
  }
  .person-role {
    position: absolute; left: 47px; top: 54px;
    font-size: 16px; line-height: 20px;
  }
  .contact-row {
    position: absolute; left: 47px; height: 22px;
    display: flex; align-items: center; font-size: 17px;
  }
  .contact-row svg { width: 16px; height: 16px; margin-right: 15px; }
  .divider {
    position: absolute; left: 306px; top: 26px; width: 1px; height: 126px;
    background: var(--rule);
  }
  .services {
    position: absolute; left: 342px; top: 24px; margin: 0; padding: 0;
    list-style: none; font-size: 17px;
  }
  .services li { height: 27.5px; line-height: 22px; }
  .services li::before { content: "»"; margin-right: 10px; font-size: 15px; }
  .address {
    position: absolute; left: 0; right: 0; top: 333px;
    text-align: center; color: var(--ink); font-size: 16px; line-height: 20px;
  }
</style>
</head>
<body>
<div class="canvas">
  <section class="card card-front">
    <div class="front-name">Brightline Site Services Ltd</div>
    <p class="specialise" style="margin:0">
      <strong>We Specialise in:</strong> Electrical/Site Temporary Electrics,<br>
      Data/Network Installation<span class="sep">|</span>Passive Fire Protection<span class="sep">|</span>Builders Works
    </p>
  </section>

  <section class="card card-back">
    <div class="brand">
      <span class="brand-square"></span>
      <span class="brand-name">Brightline Site Services Ltd</span>
    </div>

    <div class="info-band">
      <div class="person-name">Marek Nowicki</div>
      <div class="person-role">Manager Director</div>

      <div class="contact-row" style="top:85px">
        <svg viewBox="0 0 16 16" aria-hidden="true"><path fill="#fff" d="M2 6c0-2 2-3 6-3s6 1 6 3v1h-3V6H5v1H2z M4 8h8l1 5H3z"/><circle cx="8" cy="10.5" r="1.4" fill="#0a6cb0"/></svg>
        07700 900318
      </div>
      <div class="contact-row" style="top:109px">
        <svg viewBox="0 0 16 16" aria-hidden="true"><rect x="1" y="3" width="14" height="10" fill="#fff"/><path d="M1 3l7 6 7-6M1 13l5-5M15 13l-5-5" stroke="#0a6cb0" stroke-width="1.2" fill="none"/></svg>
        marek@brightlinesite.co.uk
      </div>
      <div class="contact-row" style="top:131px">
        <svg viewBox="0 0 16 16" aria-hidden="true"><circle cx="8" cy="8" r="6.5" fill="none" stroke="#fff" stroke-width="1.3"/><ellipse cx="8" cy="8" rx="3" ry="6.5" fill="none" stroke="#fff" stroke-width="1.1"/><path d="M1.5 8h13M2.5 5h11M2.5 11h11" stroke="#fff" stroke-width="1"/></svg>
        www.brightlinesite.co.uk
      </div>

      <div class="divider"></div>

      <ul class="services">
        <li>Electrical Temporary Electrics</li>
        <li>Site Temporary Electrics</li>
        <li>Data/Network Installation</li>
        <li>Passive Fire Protection</li>
        <li>Builders Works</li>
      </ul>
    </div>

    <div class="address">Fenwick Road, Marlow Green, Essex, CM99 4ZZ</div>
  </section>
</div>
</body>
</html>
```